Add Responsiveness to Current Website

The website http://www.velvet-screen-room-studio.example needs to be made responsive. This includes all the menus and all the galleries. The Design, graphics, colors can remain the same, except I can provide larger images and design for the Home Page. If you know what you are doing, this should not take too long.

Coding

Coded - Design and coding required

Number of Pages Required

5+ page

Font styles to use
Sans Serif

Colors
f37122
f78f20

Requirements
Must have
• Responsive Menus and Galleries

```html
<!DOCTYPE html>
<html lang="en">
<head>
<meta charset="utf-8">
<title>Velvet Screen — Home &amp; Art Theater Designs</title>
<link href="https://fonts.googleapis.com/css2?family=Raleway:wght@400;500;600&family=Open+Sans:wght@400;600&display=swap" rel="stylesheet">
<style>
:root{
  --orange:#f78f20;
  --orange-deep:#f37122;
  --black:#000;
  --footer:#1a1a1a;
  --footer-base:#111;
  --white:#fff;
  --text-grey:#b5b5b5;
  --muted:#6a6a6a;
}
*{margin:0;padding:0;box-sizing:border-box}
html,body{width:694px;height:1200px;overflow:hidden;background:var(--black)}
body{position:relative;font-family:"Open Sans",sans-serif;color:var(--white)}
.abs{position:absolute}
.heading{font-family:"Raleway",sans-serif}

.site-header{left:0;top:0;width:694px;height:68px;background:var(--black)}
.brand{left:139px;top:26px;display:flex;align-items:center;gap:6px;font-family:"Raleway",sans-serif;font-weight:600;font-size:19px;color:var(--orange)}
.brand-mark{width:10px;height:10px;border-radius:50%;background:var(--orange)}
.call{right:139px;top:34px;text-align:right;font-family:"Raleway",sans-serif}
.call-label{font-size:8.5px;color:var(--orange-deep)}
.call-number{font-size:11.5px;color:var(--white);display:flex;align-items:center;gap:4px;margin-top:1px}

.main-nav{left:0;top:68px;width:694px;height:26px;background:linear-gradient(#f88a2e,#f06a18)}
.main-nav ul{list-style:none;display:flex;justify-content:center;height:100%}
.main-nav li{font-family:"Raleway",sans-serif;font-weight:500;font-size:8.4px;padding:0 8px;line-height:26px;border-right:1px solid rgba(0,0,0,.15)}
.main-nav li:last-child{border-right:0}

.hero{left:0;top:94px;width:694px;height:264px;background:linear-gradient(180deg,#1e3a7a 0%,#3a3f4c 25%,#4a4a52 55%,#1c1c1e 100%)}
.hero-title{left:0;width:694px;top:95px;text-align:center;font-family:"Raleway",sans-serif;font-weight:500;font-size:25px;letter-spacing:.3px}
.hero-sub{left:0;width:694px;top:128px;text-align:center;font-family:"Raleway",sans-serif;font-weight:600;font-size:12.5px}
.hero-dots{left:326px;top:246px;display:flex;gap:3px}
.hero-dots span{width:8px;height:8px;border-radius:50%;background:var(--white)}
.hero-dots span.active{background:var(--orange)}

.about-title{left:0;width:694px;top:390px;text-align:center;font-size:15px;font-weight:500}
.about-text{left:139px;width:416px;top:413px;text-align:center;font-size:5.9px;line-height:11px;color:var(--text-grey)}
.divider{left:145px;top:491px;width:404px;height:2px;background:#1c1c1c}
.divider-knot{left:341px;top:489px;width:12px;height:5px;border:1px solid #2a2a2a;background:#111}

.feature{top:512px;width:131px;text-align:center}
.feature-img{width:131px;height:62px}
.feature-title{font-family:"Raleway",sans-serif;font-weight:500;font-size:9px;color:var(--orange);margin-top:6px}
.feature-text{font-size:5.1px;line-height:7.8px;color:var(--text-grey);margin-top:3px;padding:0 3px}
.btn{display:inline-block;margin-top:8px;width:53px;height:14px;line-height:14px;background:var(--orange-deep);font-size:5.3px;font-family:"Raleway",sans-serif;color:var(--white)}

.gallery{left:0;top:692px;width:694px;height:204px;background:var(--orange)}
.gallery-title{left:0;width:694px;top:714px;text-align:center;font-family:"Raleway",sans-serif;font-size:12px}
.thumb{width:101px;height:57px;border:2px solid var(--white)}

.reviews-title{left:0;width:694px;top:927px;text-align:center;font-family:"Raleway",sans-serif;font-size:12.5px;font-weight:500}
.review-text{left:175px;width:344px;top:953px;text-align:center;font-size:5.9px;line-height:10.7px;color:#ddd}
.review-author{left:0;width:694px;top:989px;text-align:center;font-size:6px;font-weight:600}
.stars{left:323px;top:1004px}

.site-footer{left:0;top:1046px;width:694px;height:128px;background:var(--footer);border-top:1px solid #2a2a2a}
.footer-col{top:1070px}
.footer-col h4{font-family:"Raleway",sans-serif;font-weight:500;font-size:7.4px;color:var(--orange);margin-bottom:3px}
.footer-col li{list-style:none;font-size:5.4px;line-height:11.4px;color:#ddd}
.contact-col li{font-size:6px}
.social{display:flex;gap:5px;margin-top:5px}
.social span{width:9px;height:9px;border-radius:50%;background:var(--white)}
.base{left:0;top:1174px;width:694px;height:26px;background:var(--footer-base)}
.copyright{left:152px;top:1184px;font-size:4.4px;color:var(--muted)}
</style>
</head>
<body>

<header class="abs site-header">
  <div class="abs brand"><span class="brand-mark"></span>Velvet Screen</div>
  <div class="abs call">
    <div class="call-label">Call Us Now</div>
    <div class="call-number">
      <svg width="10" height="10" viewBox="0 0 10 10"><circle cx="5" cy="5" r="4.5" fill="#555"/><path d="M3.3 2.6l1 1-.6.7c.4.8.9 1.3 1.7 1.7l.7-.6 1 1-.7.9c-1.8-.3-3.6-2.1-3.9-3.9z" fill="#111"/></svg>
      555-014-2290
    </div>
  </div>
</header>

<nav class="abs main-nav">
  <ul>
    <li>Home</li><li>Products</li><li>Gallery</li><li>Let's Begin</li><li>Acoustics</li><li>Our Story</li><li>Hospitality</li><li>Seating</li><li>Contact</li>
  </ul>
</nav>

<section class="abs hero" role="img" aria-label="Home theater room with rows of black leather recliners, framed posters and a blue starlit ceiling">
  <h1 class="abs hero-title">HOME &amp; ART THEATER DESIGNS</h1>
  <p class="abs hero-sub">MAURIS VEL LACUS VITAE FELIS VESTIBULUM</p>
  <div class="abs hero-dots"><span class="active"></span><span></span><span></span><span></span></div>
</section>

<h2 class="abs about-title heading">About Home Theater Design</h2>
<p class="abs about-text">In terms of design, your Home Theater is the most versatile room in your home. Your options are limitless. You can compliment your existing home decor or you can create a design that is completely different from the rest of your home.<br>If you enjoy exploring unique design opportunities, our decorative acoustic panels can act as a canvas for your inspiration. Marcus Delane created dozens of original artistic designs specifically for Home Theater Interiors. Perhaps, you perfer a theme for your Home Theater Design. If so, we have designed theaters devoted to Outer Space, Wine, Sports, Music, Skylines, Spy Thriller, Red Woods (and other landscapes) and more.</p>
<div class="abs divider"></div>
<div class="abs divider-knot"></div>

<article class="abs feature" style="left:139px">
  <div class="feature-img" role="img" aria-label="Theater wall with canyon landscape art panels" style="background:linear-gradient(135deg,#5a2a1c,#a0583a 50%,#3a2a24)"></div>
  <h3 class="feature-title">Your Personal Consultant</h3>
  <p class="feature-text">The moment you contact Velvet Screen, you will talk directly with Marcus Delane, the President and founder of the company. You will continue this personal dialog with Marcus throughout the entire process</p>
  <span class="btn">READ MORE</span>
</article>
<article class="abs feature" style="left:281px">
  <div class="feature-img" role="img" aria-label="Custom wall panels lit by warm sconces" style="background:linear-gradient(135deg,#4a3a26,#8a7352 50%,#3a2e20)"></div>
  <h3 class="feature-title">Custom Panels and Designs</h3>
  <p class="feature-text">The moment you contact Velvet Screen, you will talk directly with Marcus Delane, the President and founder of the company. You will continue this personal dialog with Marcus throughout the entire process</p>
  <span class="btn">READ MORE</span>
</article>
<article class="abs feature" style="left:423px">
  <div class="feature-img" role="img" aria-label="Theater wall with warm lit art panel and sconce" style="background:linear-gradient(135deg,#3a2616,#9a7450 50%,#4a3220)"></div>
  <h3 class="feature-title">Home Movie Theater Products</h3>
  <p class="feature-text">The moment you contact Velvet Screen, you will talk directly with Marcus Delane, the President and founder of the company. You will continue this personal dialog with Marcus throughout the entire process</p>
  <span class="btn">READ MORE</span>
</article>

<section class="abs gallery"></section>
<svg class="abs" style="left:332px;top:692px" width="30" height="12" viewBox="0 0 30 12"><path d="M0 0h30L15 12z" fill="#000"/></svg>
<h2 class="abs gallery-title">PHOTO GALLERY</h2>
<div class="abs thumb" style="left:141px;top:742px;background:linear-gradient(135deg,#2a1a12,#6a4a2a)" role="img" aria-label="Theater with colorful art panels"></div>
<div class="abs thumb" style="left:246px;top:742px;background:linear-gradient(135deg,#5a1a14,#2a3a6a)" role="img" aria-label="Theater with red and blue art panels"></div>
<div class="abs thumb" style="left:352px;top:742px;background:linear-gradient(135deg,#3a2a1a,#8a6a48)" role="img" aria-label="Theater screen wall with wood paneling"></div>
<div class="abs thumb" style="left:458px;top:742px;background:linear-gradient(135deg,#3a3040,#6a5060)" role="img" aria-label="Theater seating with purple art panels"></div>
<div class="abs thumb" style="left:141px;top:804px;background:linear-gradient(135deg,#2a2216,#7a6a3a)" role="img" aria-label="Theater with abstract square art panels"></div>
<div class="abs thumb" style="left:246px;top:804px;background:linear-gradient(135deg,#3a2618,#7a5a3a)" role="img" aria-label="Theater with circular art panels"></div>
<div class="abs thumb" style="left:352px;top:804px;background:linear-gradient(135deg,#2a2016,#5a4a36)" role="img" aria-label="Theater with tiered seating rows"></div>
<div class="abs thumb" style="left:458px;top:804px;background:linear-gradient(135deg,#3a3020,#8a7650)" role="img" aria-label="Theater with patterned wall panels"></div>

<h2 class="abs reviews-title">Customer Reviews</h2>
<svg class="abs" style="left:148px;top:947px" width="14" height="32" viewBox="0 0 14 32"><path d="M13 1L1 16l12 15" fill="none" stroke="#ccc" stroke-width="1"/></svg>
<svg class="abs" style="left:534px;top:947px" width="14" height="32" viewBox="0 0 14 32"><path d="M1 1l12 15L1 31" fill="none" stroke="#ccc" stroke-width="1"/></svg>
<p class="abs review-text">In massa libero interdum nec interdum vel blandit sed nulla In ullamcorper est eget tempor cursus neque mi consectetuer mi a ultricies massa est sed nisl Class aptent taciti sociosqu ad litora torquent per conubia nostra per inceptos hymenaeos Proin nulla arcu nonummy luctus dictum eget fermentum et lorem</p>
<p class="abs review-author">By Author Name</p>
<svg class="abs stars" width="48" height="9" viewBox="0 0 48 9">
  <defs><path id="star" d="M4.5 0l1.1 3.1H9L6.3 5l1 3.4-2.8-2-2.8 2 1-3.4L0 3.1h3.4z"/></defs>
  <use href="#star" x="0" fill="#f78f20"/><use href="#star" x="9.5" fill="#f78f20"/><use href="#star" x="19" fill="#f78f20"/><use href="#star" x="28.5" fill="#f78f20"/><use href="#star" x="38" fill="#fff"/>
</svg>

<footer class="abs site-footer"></footer>
<div class="abs footer-col" style="left:153px"><h4>DESIGNS</h4><ul><li>Artesian Panels</li><li>Themes</li><li>Universal Theme</li><li>Completed Projects</li><li>Custom Theaters</li><li>Conventional Fabricsa</li></ul></div>
<div class="abs footer-col" style="left:246px"><h4>COMPANY</h4><ul><li>About Company</li><li>Customer Review</li><li>Contact</li><li>Company History</li></ul></div>
<div class="abs footer-col" style="left:328px"><h4>RESOURCES</h4><ul><li>Hospitality</li><li>Seating</li><li>Gallery</li><li>Products</li><li>Let's Begin</li></ul></div>
<div class="abs footer-col contact-col" style="left:410px"><h4>GET IN TOUCH</h4><ul><li>412 Harbor Palm Way</li><li>Coral Vista, FL</li><li>Phone: 555-014-2290</li><li>Email: marcus@velvetscreen.example</li></ul>
  <div class="social" aria-label="Social links"><span></span><span></span><span></span><span></span></div>
</div>
<div class="abs base"></div>
<p class="abs copyright">© 2015 Company Name  All rights reserved  Term of Use</p>

</body>
</html>
```